Postcard for Lawn service business

I am starting a lawn service business and need a professional looking postcard with a logo.

Thank you for any help you can provide.

We are looking for someone to design a long term professional marketable original business logo. One that can be trademarked in the future. Right now we are going with “the silver furrow” lawn service. This is a new start up company that will provide mowing and basic lawn service care as well as full service maintenance on other shrubs/plants on residential property.

We are also looking for a professional looking glossy oversized postcard to direct mail to potential customers through NMDR mail routes. I am open to any professional design ideas, we've provided actual pictures of grass and myself. I would like to keep it personal to the working homeowner, possible small family that doesn’t need to bother with this weekly chore.

Here is an idea for a slogan: "You work hard, let us take care of your yard". Or if you have a better idea.

Suggested verbiage (we like all of them but all may not fit):
Free Estimates- Evening and Weekend Appointments available Call 555-208-4419 or Email TheSilverFurrow@quillpost.com
Services to fit your needs; Basic and Full Service rates available
Fertilization and Maintenance Services for Residential Properties in Corona
Services offered: Mow/Edge/Blow, Fertilization, Weed Control, Yard Cleanups, Hedge Trimming,
Family and Locally owned and operated
Referral savings opportunity! For each friend that receives our monthly lawn service, save $5 off your monthly service for a max savings of $20 a month. Keep this monthly discount for as long as your friends are our customers!

Target Market(s)

We are targeting dual income families that can save time by having someone else provide care for their lawn. We need catchy call to action lines to get them to switch to our service vs their current lawn care providers.

Industry/Entity Type

Residential

Requirements
Must have
• The flyer must be a two sided colorful oversized postcard.
Nice to have
• Would like to see the pantone green used with white throughout the flyer.
PANTONE
16-6138 TCX

Would like similar color feel as flyer2 (file attached)
We like to call-outs feel on flyer3 (file attached)
Img 2150 is a pic of me with our lawn, either keep the whole pic or just me
Dustin1 is a pic of me digging up a tree stump
lawn1, lawn2, lawn3, and lawn4 are shots of grass, can be used as background or something else

```html
<!DOCTYPE html>
<html lang="en">
<head>
<meta charset="utf-8">
<title>The Silver Furrow Yard Care – Postcard</title>
<link href="https://fonts.googleapis.com/css2?family=Titan+One&family=Josefin+Sans:wght@400;600&family=Fjalla+One&family=Kaushan+Script&family=Exo+2:ital,wght@1,700&display=swap" rel="stylesheet">
<style>
  :root {
    --paper: #fefde6;
    --brown: #4a2f22;
    --green: #4d7a3c;
    --slate: #98a3a1;
    --brick: #b5352b;
    --rule: #444;
  }
  * { margin: 0; padding: 0; box-sizing: border-box; }
  html, body { width: 1200px; height: 851px; overflow: hidden; background: var(--paper); }
  .postcard { position: relative; width: 1200px; height: 851px; background: var(--paper); color: var(--brown); }
  .divider { position: absolute; left: 591px; top: 0; width: 1px; height: 851px; background: var(--rule); }
  .abs { position: absolute; white-space: nowrap; }

  /* Front panel */
  .tagline-top { left: 82px; top: 30px; font: 400 38px "Titan One", sans-serif; color: var(--brown); }
  .tagline-big { left: 64px; top: 60px; font: 400 98px/1 "Titan One", sans-serif; color: var(--green); }
  .tagline-end { left: 140px; top: 156px; font: 600 36px "Josefin Sans", sans-serif; color: var(--brown); }
  .tagline-end .accent { font-size: 52px; text-decoration: underline; text-decoration-thickness: 3px; text-underline-offset: 4px; }
  .thanks { left: 160px; top: 246px; font: 600 16px "Josefin Sans", sans-serif; }

  .name-block { display: flex; align-items: center; gap: 12px; }
  .name-dot { flex: none; border-radius: 50%; }
  .name-text { font-family: "Josefin Sans", sans-serif; font-weight: 600; line-height: 1.15; }

  .front-name { left: 160px; top: 280px; color: var(--brown); }
  .front-name .name-dot { width: 26px; height: 26px; background: var(--brown); }
  .front-name .name-text { font-size: 36px; }
  .front-name .name-sub { display: block; font-size: 17px; letter-spacing: 3px; margin-top: 6px; }

  .services-title { left: 0; width: 591px; top: 466px; text-align: center; font: 400 29px "Fjalla One", sans-serif; color: var(--brown); }
  .services-list { left: 0; width: 591px; top: 520px; text-align: center; list-style: none; font: 400 28px/31px "Josefin Sans", sans-serif; color: var(--green); }
  .phone { left: 0; width: 591px; top: 704px; text-align: center; font: 400 31px "Josefin Sans", sans-serif; color: var(--brown); }
  .cta { left: 0; width: 591px; top: 746px; text-align: center; font: 400 50px "Fjalla One", sans-serif; color: var(--brown); }

  /* Back panel */
  .ownership { right: 9px; top: 6px; font: italic 700 19px "Exo 2", sans-serif; color: var(--brown); }
  .back-name { left: 591px; width: 609px; top: 110px; justify-content: center; color: var(--slate); }
  .back-name .name-dot { width: 54px; height: 54px; background: var(--slate); }
  .back-name .name-text { font-size: 62px; }
  .back-name .name-sub { display: block; font-size: 30px; letter-spacing: 6px; margin-top: 10px; }

  .referral { left: 612px; top: 384px; width: 570px; white-space: normal; font: 400 28.5px/69px "Kaushan Script", cursive; color: var(--brick); text-decoration: underline dotted #777; text-underline-offset: 9px; }
  .email { left: 591px; width: 609px; top: 795px; text-align: center; font: 400 32px "Fjalla One", sans-serif; color: var(--brown); }
</style>
</head>
<body>
<main class="postcard">
  <section class="front-panel">
    <p class="abs tagline-top">The grass is</p>
    <p class="abs tagline-big">Greener</p>
    <p class="abs tagline-end">on <span class="accent">your</span> side ,</p>
    <p class="abs thanks">Thanks to</p>
    <div class="abs name-block front-name">
      <span class="name-dot"></span>
      <p class="name-text">The Silver Furrow<span class="name-sub">YARD CARE</span></p>
    </div>
    <h2 class="abs services-title">Services Include;</h2>
    <ul class="abs services-list">
      <li>mow/edge/blow</li>
      <li>fertilization</li>
      <li>weed control</li>
      <li>yard cleanups</li>
      <li>hedge-trimming.</li>
    </ul>
    <p class="abs phone">555-208-4419</p>
    <p class="abs cta">Call Now!</p>
  </section>

  <div class="divider"></div>

  <section class="back-panel">
    <p class="abs ownership">FAMILY AND LOCALLY OWNED AND OPERATED</p>
    <div class="abs name-block back-name">
      <span class="name-dot"></span>
      <p class="name-text">The Silver Furrow<span class="name-sub">YARD CARE</span></p>
    </div>
    <p class="abs referral">Referral savings opportunity! For each friend that receives our monthly lawn service, save $5 off your monthly service for a max savings of $20 a month. Keep this monthly discount for as long as your friends are our customers!</p>
    <p class="abs email">TheSilverFurrow@quillpost.com</p>
  </section>
</main>
</body>
</html>
```